Young Architect Bussiness Card

English is not my first language (spanish is).
Need a bussiness card design for my best friend who is about to graduate from college, Licentiate degree in architecture, so she needs business cards to start networking, currently she has no porfolio, web page or facebook. so she is relying on her cel phone and gmail, but should leave space for one of them (facebook)

Design for business card should be modern, maybe something with construction blue prints patern or 3D modelling.

Name: Mariela Ocampo Valverde
Licentiate in Arquitecture
Cel: (506) XXX-8270
email: marielaXXX@correonube.net

Services, although im not sure if it has to be there or not:
Anteproyectos / Proposal design
Inspecciones / Site Inspections
Modelado 3D / 3D modelling
Planos Constructivos / Construction Blue Prints
Presupuestos / Budgets

Design should be in spanish

Industry/Entity Type

Architect

Contact Information for Business Card

Name: Mariela Ocampo, Arquitecto
Associtation code : XXXX
Phone: (506) XXXX-XXXX
Email: xxx@correonube.net
Facebook: xxxx

Requirements
Must have
• Design for business card should be modern, maybe something with construction blue prints patern or 3D modelling.
Nice to have
• Something like a transition from 2D to 3D.

```html
<!DOCTYPE html>
<html lang="es">
<head>
<meta charset="utf-8">
<title>Mariela Ocampo · Arquitecto</title>
<link href="https://fonts.googleapis.com/css2?family=IBM+Plex+Mono:wght@300;400;700&display=swap" rel="stylesheet">
<style>
  :root {
    --yellow: #f2c230;
    --ink: #111111;
    --white: #ffffff;
    --page: #e9e6e1;
    --sheet-1: #f6f7f8;
    --sheet-2: #dfe4ea;
    --sheet-3: #c9d2dc;
    --helmet: #f0a030;
  }
  * { box-sizing: border-box; margin: 0; padding: 0; }
  html, body {
    width: 1200px; height: 900px; overflow: hidden;
    background: var(--page);
    font-family: "IBM Plex Mono", monospace;
  }
  .card {
    position: absolute; left: 250px; width: 700px; height: 400px;
    overflow: hidden; box-shadow: 0 6px 18px rgba(0,0,0,.18);
  }
  .card--front { top: 30px; background: var(--yellow); }
  .card--back { top: 470px; }

  .band { position: absolute; inset: 0; width: 100%; height: 100%; }

  .identity { position: absolute; display: flex; align-items: flex-start; }
  .identity__mark { background: var(--ink); flex: none; }
  .identity__text { line-height: 1; color: var(--ink); }
  .identity__name { font-weight: 700; text-transform: uppercase; }
  .identity__role { font-weight: 300; margin-top: 10px; }

  .card--front .identity { left: 40px; top: 70px; gap: 14px; }
  .card--front .identity__mark { width: 14px; height: 14px; margin-top: 8px; }
  .card--front .identity__name { font-size: 32px; }
  .card--front .identity__name + .identity__name { margin-top: 4px; }
  .card--front .identity__role { font-size: 18px; }

  .card--back .identity { left: 300px; top: 120px; gap: 20px; }
  .card--back .identity__mark { width: 22px; height: 22px; margin-top: 12px; }
  .card--back .identity__name { font-size: 52px; }
  .card--back .identity__name + .identity__name { margin-top: 6px; }
  .card--back .identity__role { font-size: 28px; margin-top: 16px; }

  .contact {
    position: absolute; left: 390px; top: 40px;
    list-style: none; font-size: 15px; color: var(--ink); line-height: 1;
  }
  .contact li { margin-bottom: 18px; }
  .contact b { font-weight: 700; }
  .contact span { font-weight: 300; }

  .service {
    position: absolute; font-weight: 700; font-size: 20px; line-height: 1;
    color: var(--white); white-space: nowrap;
  }
  .service--accent { color: var(--yellow); }

  .artwork {
    position: absolute; inset: 0;
    background:
      linear-gradient(160deg, transparent 62%, rgba(240,160,48,.55) 100%),
      linear-gradient(20deg, rgba(242,194,48,.35) 0%, transparent 30%),
      linear-gradient(135deg, var(--sheet-1) 0%, var(--sheet-2) 60%, var(--sheet-3) 100%);
  }
</style>
</head>
<body>

<section class="card card--front">
  <svg class="band" viewBox="0 0 700 400" aria-hidden="true">
    <polygon points="0,300 380,245 380,215 700,165 700,400 0,400" fill="var(--ink)"/>
  </svg>

  <div class="identity">
    <div class="identity__mark"></div>
    <div class="identity__text">
      <div class="identity__name">Mariela</div>
      <div class="identity__name">Ocampo</div>
      <div class="identity__role">Arquitecto</div>
    </div>
  </div>

  <ul class="contact">
    <li><b>Associtation code :</b> <span>XXXX</span></li>
    <li><b>Phone:</b> <span>(506) XXXX-XXXX</span></li>
    <li><b>Email:</b> <span>xxx@correonube.net</span></li>
    <li><b>Facebook:</b> <span>xxxx</span></li>
  </ul>

  <div class="service" style="left:530px; top:200px;">Modelado 3D</div>
  <div class="service service--accent" style="left:392px; top:258px;">Inspecciones</div>
  <div class="service" style="left:440px; top:294px;">Planos Constructivos</div>
  <div class="service" style="left:40px; top:330px;">Anteproyectos</div>
  <div class="service service--accent" style="left:185px; top:364px;">Presupuestos</div>
</section>

<section class="card card--back">
  <div class="artwork" role="img" aria-label="Ilustración de mesa de arquitecto sobre planos constructivos: casco de obra, nivel, cinta métrica, lápices y muestrario de colores"></div>
  <div class="identity">
    <div class="identity__mark"></div>
    <div class="identity__text">
      <div class="identity__name">Mariela</div>
      <div class="identity__name">Ocampo</div>
      <div class="identity__role">Arquitecto</div>
    </div>
  </div>
</section>

</body>
</html>
```